Brookmere Osteopathy flyer

I want a clean clear DL flyer (but also want an A4 poster) promoting a new Osteopathic business in a semi rural area in Tasmania (Australia).
It can have pictures like the examples attached to show people what Osteopathy is (its like Chiropractic and physiotherapy).
I am the sole practioner and am male, so any pictures would be best to be a white male if possible.
I've attached some wording, you can use all, or none of it
I don't have a phone number for the business yet
info@brookmereosteopathy.example
www.brookmereosteopathy.example
Target Market(s)
Australians, from tradies, professionals, babies to retired people
Industry/Entity Type
Health
Look and feel

```html
<!DOCTYPE html>
<html lang="en">
<head>
<meta charset="utf-8">
<title>Brookmere Osteopathy – DL Flyer</title>
<link rel="stylesheet" href="https://fonts.googleapis.com/css2?family=Lato:wght@400;700&display=swap">
<style>
  :root {
    --stage: #a3a3a3;
    --paper: #ffffff;
    --blue-deep: #1577b8;
    --blue-mid: #1f8fd0;
    --blue-light: #3aa6e0;
    --brand-blue: #2a9ad8;
    --skin-light: #e9c8a8;
    --skin-mid: #c99a76;
    --text-light: #ffffff;
    --text-soft: #e8f4fc;
  }
  * { margin: 0; padding: 0; box-sizing: border-box; }
  html, body { width: 1200px; height: 1200px; overflow: hidden; }
  body {
    background: var(--stage);
    font-family: "Lato", Arial, sans-serif;
    position: relative;
  }
  .flyer {
    position: absolute;
    left: 348px; top: 65px;
    width: 505px; height: 1070px;
    overflow: hidden;
    background: linear-gradient(180deg, var(--blue-deep) 0%, var(--blue-mid) 50%, var(--blue-light) 100%);
  }
  .flyer-art { position: absolute; left: 0; top: 0; }
  .brand {
    position: absolute;
    left: 262px; top: 84px;
    width: 200px;
    display: flex; align-items: center; gap: 10px;
    color: var(--brand-blue);
    font-weight: 700; font-size: 19px; line-height: 1.15;
  }
  .brand-dot {
    flex: none; width: 18px; height: 18px;
    border-radius: 50%; background: var(--brand-blue);
  }
  .reasons {
    position: absolute; left: 0; top: 574px; width: 100%;
    color: var(--text-light);
  }
  .reasons-title {
    text-align: center; font-weight: 700; font-size: 16.5px;
    margin-bottom: 18px;
  }
  .reasons-list {
    list-style: none;
    margin-left: 155px;
    font-size: 13.5px; line-height: 17.5px;
    color: var(--text-soft);
  }
  .reasons-list li { position: relative; }
  .reasons-list li::before {
    content: ""; position: absolute; left: -31px; top: 7px;
    width: 4px; height: 4px; border-radius: 50%; background: var(--text-soft);
  }
  .about {
    position: absolute; left: 50px; top: 828px; width: 405px;
    text-align: center; font-size: 13.5px; line-height: 17.5px;
    color: var(--text-soft);
  }
  .divider {
    position: absolute; left: 106px; top: 916px; width: 293px;
    height: 1.5px; background: var(--text-light);
  }
  .contact-icons {
    position: absolute; left: 0; top: 934px; width: 100%;
    display: flex; justify-content: center; gap: 14px;
  }
  .contact-icons svg { width: 16px; height: 16px; fill: var(--text-light); }
  .contact {
    position: absolute; left: 0; top: 968px; width: 100%;
    text-align: center; font-size: 13.5px; line-height: 17px;
    color: var(--text-soft);
  }
</style>
</head>
<body>
  <main class="flyer">
    <svg class="flyer-art" width="505" height="1070" viewBox="0 0 505 1070">
      <defs>
        <linearGradient id="treatment-photo-tone" x1="0" y1="0" x2="0" y2="1">
          <stop offset="0" stop-color="var(--skin-light)"/>
          <stop offset="0.55" stop-color="var(--skin-mid)"/>
          <stop offset="1" stop-color="var(--blue-deep)" stop-opacity="0"/>
        </linearGradient>
        <linearGradient id="hands-photo-tone" x1="0" y1="0" x2="1" y2="1">
          <stop offset="0" stop-color="#f0d5bb"/>
          <stop offset="1" stop-color="#c08c68"/>
        </linearGradient>
        <clipPath id="inset-clip"><circle cx="96" cy="348" r="158"/></clipPath>
      </defs>
      <rect class="treatment-photo" x="0" y="230" width="505" height="380"
            fill="url(#treatment-photo-tone)" role="img"
            aria-label="Photo: osteopath's hands treating a patient's lower back"/>
      <path class="header-panel" d="M0 0 H505 V300 C420 360 230 390 0 250 Z" fill="var(--paper)"/>
      <circle cx="96" cy="348" r="164" fill="var(--paper)"/>
      <rect class="inset-photo" x="-70" y="190" width="330" height="320"
            clip-path="url(#inset-clip)" fill="url(#hands-photo-tone)" role="img"
            aria-label="Photo: practitioner's hands applying spinal manipulation"/>
    </svg>

    <div class="brand"><span class="brand-dot"></span><span>Brookmere Osteopathy</span></div>

    <section class="reasons">
      <h2 class="reasons-title">Common reasons people visit an osteopath:</h2>
      <ul class="reasons-list">
        <li>Back / neck pain</li>
        <li>Headaches / migraines</li>
        <li>Joint and muscle pain</li>
        <li>Pregnancy-related discomfort</li>
        <li>Disc related issues</li>
        <li>Sciatica</li>
        <li>Plantar fasciitis</li>
        <li>Tendonitis / Bursitis</li>
        <li>Adhesive capsulitis (frozen shoulder)</li>
        <li>Tennis / Golfers elbow</li>
      </ul>
    </section>

    <p class="about">Osteopaths use a combination of joint manipulation, targeted deep tissue massage and stretching to improve function, relieve pain and support the body's ability to heal itself.</p>

    <div class="divider"></div>

    <div class="contact-icons">
      <svg viewBox="0 0 16 16" aria-label="Address"><path d="M8 0a5.5 5.5 0 0 0-5.5 5.5C2.5 10 8 16 8 16s5.5-6 5.5-10.5A5.5 5.5 0 0 0 8 0zm0 7.8a2.3 2.3 0 1 1 0-4.6 2.3 2.3 0 0 1 0 4.6z"/></svg>
      <svg viewBox="0 0 16 16" aria-label="Phone"><path d="M3.6 1 6 3.6 4.8 5.6c.9 2 2.6 3.7 4.6 4.6l2-1.2L14 11.4 12.6 14C6.6 14 2 9.4 2 3.4z"/></svg>
      <svg viewBox="0 0 16 16" aria-label="Email"><path d="M1 3h14v1.2L8 9 1 4.2zM1 5.8l7 4.7 7-4.7V13H1z"/></svg>
      <svg viewBox="0 0 16 16" aria-label="Website"><path d="M8 1a7 7 0 1 0 0 14A7 7 0 0 0 8 1zm0 1.6c.9 1 1.5 2.6 1.7 4.6H6.3C6.5 5.2 7.1 3.6 8 2.6zM2.7 8.8h2.1c.1 1.6.5 3 1.1 4.1a5.4 5.4 0 0 1-3.2-4.1zm0-1.6a5.4 5.4 0 0 1 3.2-4.1c-.6 1.1-1 2.5-1.1 4.1zm5.3 6.2c-.9-1-1.5-2.6-1.7-4.6h3.4c-.2 2-.8 3.6-1.7 4.6zm2.1-.5c.6-1.1 1-2.5 1.1-4.1h2.1a5.4 5.4 0 0 1-3.2 4.1zm1.1-5.7c-.1-1.6-.5-3-1.1-4.1a5.4 5.4 0 0 1 3.2 4.1z"/></svg>
    </div>

    <address class="contact" style="font-style:normal">
      24 Mill Creek Road, Brookmere<br>
      Insert Phone Number<br>
      www.brookmereosteopathy.example<br>
      info@brookmereosteopathy.example
    </address>
  </main>
</body>
</html>
```